Brintell's Business Card

I need some designs for a new business card including the new logo attached. An old example of our business card is also attached to show all the data that should be included on the new design.
**I added some more examples someone had mocked up**

Contact Information for Business Card

Should include all info on other examples uploaded.

```html
<!DOCTYPE html>
<html lang="en">
<head>
<meta charset="utf-8">
<title>Brintell's Business Card</title>
<link href="https://fonts.googleapis.com/css2?family=Montserrat:wght@400;500;600;700&display=swap" rel="stylesheet">
<style>
  :root {
    --backdrop: #e9e6e1;
    --card: #262626;
    --blue: #1673be;
    --red: #e3262a;
    --white: #ffffff;
    --ghost: #3f3f3f;
    --divider: #8a8a8a;
  }
  * { margin: 0; padding: 0; box-sizing: border-box; }
  html, body { width: 900px; height: 1200px; overflow: hidden; }
  body {
    position: relative;
    background: var(--backdrop);
    font-family: "Montserrat", sans-serif;
  }
  .card {
    position: absolute;
    left: 78px;
    width: 744px;
    height: 442px;
    border-radius: 30px;
    background: var(--card);
    overflow: hidden;
  }
  .card-front { top: 130px; }
  .card-back { top: 638px; }

  .brand { position: absolute; display: flex; align-items: center; }
  .brand-mark { width: 118px; height: 118px; border-radius: 50%; flex: none; }
  .brand-text { margin-left: 22px; }
  .brand-name {
    font-weight: 700;
    font-size: 62px;
    line-height: 62px;
    letter-spacing: 1px;
  }
  .brand-tagline {
    font-weight: 600;
    font-size: 18.5px;
    margin-top: 6px;
    letter-spacing: 0.2px;
  }
  .card-front .brand { left: 90px; top: 108px; }
  .card-front .brand-mark { background: var(--blue); }
  .card-front .brand-name { color: var(--blue); }
  .card-front .brand-tagline { color: var(--red); }

  .card-back .brand { left: 84px; top: 176px; }
  .card-back .brand-mark { background: var(--ghost); }
  .card-back .brand-name, .card-back .brand-tagline { color: var(--ghost); }

  .person {
    position: absolute;
    left: 162px; top: 316px;
    color: var(--blue);
    font-weight: 700;
    font-size: 25px;
  }
  .divider {
    position: absolute;
    left: 374px; top: 309px;
    width: 1.5px; height: 40px;
    background: var(--divider);
  }
  .contact { position: absolute; left: 400px; top: 305px; color: var(--white); font-size: 16.5px; }
  .contact-row { display: flex; align-items: center; height: 23px; }
  .contact-row svg { width: 15px; height: 13px; margin-right: 10px; flex: none; }

  .band { position: absolute; left: 0; bottom: 0; width: 744px; height: 42px; }
  .band-label {
    position: absolute; bottom: 10px;
    color: var(--white); font-size: 16px; font-weight: 500; letter-spacing: 0.3px;
  }
  .band-label-left { left: 98px; }
  .band-label-right { left: 432px; }

  .back-stripe {
    position: absolute; left: 0; bottom: 0;
    width: 100%; height: 8px; background: var(--red);
  }
</style>
</head>
<body>
  <section class="card card-front">
    <div class="brand">
      <div class="brand-mark"></div>
      <div class="brand-text">
        <div class="brand-name">BRINTELL'S</div>
        <div class="brand-tagline">AIR CONDITIONING &amp; HEATING SERVICE</div>
      </div>
    </div>

    <div class="person">Dale Brintell</div>
    <div class="divider"></div>
    <div class="contact">
      <div class="contact-row">
        <svg viewBox="0 0 15 13" aria-hidden="true"><path d="M1 4 Q7.5 -1 14 4 L12 6 L10 4.5 L5 4.5 L3 6 Z M3 7 L12 7 L13 12 L2 12 Z" fill="var(--red)"/></svg>
        <span>555.014.2290</span>
      </div>
      <div class="contact-row">
        <svg viewBox="0 0 15 13" aria-hidden="true"><rect x="1" y="2" width="13" height="9" fill="var(--blue)"/><path d="M1 2 L7.5 7 L14 2" stroke="var(--card)" stroke-width="1.2" fill="none"/></svg>
        <span>hvacbrintell@mailbox.com</span>
      </div>
    </div>

    <svg class="band" viewBox="0 0 744 42" aria-hidden="true">
      <polygon points="0,0 396,0 374,42 0,42" fill="var(--blue)"/>
      <polygon points="400,0 744,0 744,42 378,42" fill="var(--red)"/>
    </svg>
    <div class="band-label band-label-left">LICENSED &amp; INSURED</div>
    <div class="band-label band-label-right">FAMILY OWNED &amp; OPERATED</div>
  </section>

  <section class="card card-back">
    <div class="brand">
      <div class="brand-mark"></div>
      <div class="brand-text">
        <div class="brand-name">BRINTELL'S</div>
        <div class="brand-tagline">AIR CONDITIONING &amp; HEATING SERVICE</div>
      </div>
    </div>
    <div class="back-stripe"></div>
  </section>
</body>
</html>
```